Ferris Contracting LLC Business Card Design

I am looking for a creative and unique business card design. We are a commercial construction general contractor. With the name "FERRIS" Contracting, I am hoping to see some neat designs that correlate with the name.

```html
<!DOCTYPE html>
<html lang="en">
<head>
<meta charset="utf-8">
<title>Ferris Contracting LLC – Business Card</title>
<link rel="stylesheet" href="https://fonts.googleapis.com/css2?family=Montserrat:wght@400;500;700;800&display=swap">
<style>
  :root {
    --stage: #2b2b2d;
    --card-dark: #121214;
    --card-light: #d9d9db;
    --brand-blue: #1f8fe0;
    --text-light: #f2f2f2;
    --emboss: #bcbcbf;
  }
  * { margin: 0; padding: 0; box-sizing: border-box; }
  html, body {
    width: 1200px; height: 900px; overflow: hidden;
    background: var(--stage);
    font-family: "Montserrat", Arial, sans-serif;
  }
  .sheet {
    width: 1200px; height: 900px;
    display: flex; flex-direction: column;
    align-items: center; justify-content: center; gap: 56px;
  }
  .card {
    width: 600px; height: 343px;
    border-radius: 22px;
    position: relative;
    box-shadow: 0 14px 30px rgba(0,0,0,.45);
  }
  .card--front { background: var(--card-dark); color: var(--text-light); }
  .card--back { background: var(--card-light); display: flex; align-items: center; justify-content: center; }

  .contact { position: absolute; left: 44px; top: 40px; }
  .contact__name { color: var(--brand-blue); font-weight: 700; font-size: 27px; line-height: 1.1; }
  .contact__title { font-size: 14px; font-weight: 400; margin-top: 4px; }
  .contact__address { font-size: 14px; line-height: 1.45; margin-top: 26px; }
  .contact__list { list-style: none; margin-top: 24px; font-size: 14px; line-height: 1.9; }
  .contact__list li { display: flex; align-items: center; gap: 10px; }
  .contact__list svg { width: 13px; height: 13px; fill: var(--brand-blue); flex: none; }

  .wordmark {
    position: absolute; right: 42px; bottom: 66px;
    display: flex; align-items: center; gap: 14px;
  }
  .wordmark__dot { width: 22px; height: 22px; border-radius: 50%; background: var(--brand-blue); }
  .wordmark__text {
    color: var(--brand-blue); font-weight: 800; font-size: 44px;
    line-height: 1; letter-spacing: 1px;
  }
  .wordmark__sub { display: block; font-size: 15px; letter-spacing: 7px; margin-top: 6px; }

  .wordmark--emboss { position: static; }
  .wordmark--emboss .wordmark__dot { background: var(--emboss); width: 30px; height: 30px; }
  .wordmark--emboss .wordmark__text { color: var(--emboss); font-size: 62px; }
  .wordmark--emboss .wordmark__sub { font-size: 20px; letter-spacing: 10px; }
</style>
</head>
<body>
<main class="sheet">
  <section class="card card--front">
    <div class="contact">
      <p class="contact__name">Dean Holloway</p>
      <p class="contact__title">Managing Director</p>
      <p class="contact__address">Your address, City<br>State, Zip 1234</p>
      <ul class="contact__list">
        <li>
          <svg viewBox="0 0 16 16" aria-hidden="true"><path d="M3.5 1l3 3-2 2c1 2 3 4 5 5l2-2 3 3-2 3C7 14 2 9 1 3.5z"/></svg>
          123 456 789
        </li>
        <li>
          <svg viewBox="0 0 16 16" aria-hidden="true"><path d="M1 3h14v10H1z M1 3l7 6 7-6" stroke="#121214" stroke-width="1.2"/></svg>
          info@ferriscontracting.com
        </li>
        <li>
          <svg viewBox="0 0 16 16" aria-hidden="true"><circle cx="8" cy="8" r="7"/></svg>
          www.ferriscontracting.com
        </li>
      </ul>
    </div>
    <div class="wordmark">
      <span class="wordmark__dot"></span>
      <p class="wordmark__text">FERRIS<span class="wordmark__sub">CONTRACTING</span></p>
    </div>
  </section>

  <section class="card card--back">
    <div class="wordmark wordmark--emboss">
      <span class="wordmark__dot"></span>
      <p class="wordmark__text">FERRIS<span class="wordmark__sub">CONTRACTING</span></p>
    </div>
  </section>
</main>
</body>
</html>
```